Bright Hollow is a Smart Device integration/installation business

Hi, I am a tech enthusiast with a background in robotics, industrial automation and computers. I have currently launched a business to bring wireless voice controlled devices and smart devices into peoples homes at affordable prices, moving away from expensive smart wiring and programming installations. I fix bad wifi in houses and install new smart locks, multi-room audio, automated blinds etc. that can all be controlled through nimbo (carrowby) or Pellix Hub.

I need a modern and eye catching a5 flyer developed for post box drops that give people an understanding of what smart devices are - pellix hub, carrowby nimbo etc and how it can improve their lives. I have a couple of examples that I put together before realising that I need professional help. So please use these as a guide if they are helpful.

My website which also needs some work is: www.brighthollow-example.net for some more ideas and info on the services I supply. I also have a facebook page with that business name for some recent posts.

If you need anymore info or idea on what I do let me know, cheers.

Target Market(s)

Pre-exisiting homes

Industry/Entity Type

Technology Equipment

Requirements
Must have
• My logo and business details mob and website

```html
<!DOCTYPE html>
<html lang="en">
<head>
<meta charset="utf-8">
<title>Bright Hollow – Smart Home Flyers</title>
<link href="https://fonts.googleapis.com/css2?family=Roboto+Condensed:wght@400;700&family=Open+Sans:wght@400;600&display=swap" rel="stylesheet">
<style>
  :root{
    --blue:#1e9bd7;
    --blue-deep:#1466a8;
    --navy:#16457e;
    --ink:#222428;
    --panel:#26282c;
    --text:#2c2c2c;
    --white:#ffffff;
    --bg:#e9eaec;
    --rule:#dcdfe3;
  }
  *{box-sizing:border-box;margin:0;padding:0}
  html,body{width:977px;height:1200px;overflow:hidden;background:var(--bg)}
  body{position:relative;font-family:"Open Sans",sans-serif;color:var(--text)}
  .flyer{position:absolute;top:275px;width:460px;height:650px;background:var(--white);overflow:hidden;box-shadow:0 4px 14px rgba(0,0,0,.18)}
  .flyer--front{left:20px}
  .flyer--back{left:497px}
  .abs{position:absolute}
  .cond{font-family:"Roboto Condensed",sans-serif}
  .ph{position:absolute;display:block}

  /* brand */
  .brand{position:absolute;display:flex;align-items:center;gap:8px}
  .brand__dot{width:30px;height:30px;border-radius:50%;background:var(--blue)}
  .brand__name{font-family:"Roboto Condensed",sans-serif;font-weight:700;font-size:25px;letter-spacing:1.5px;color:var(--navy);text-transform:uppercase;line-height:1}

  /* front */
  .kicker{left:18px;top:24px;font-size:15px;letter-spacing:.3px;color:#555;font-family:"Open Sans",sans-serif}
  .kicker b{color:var(--blue);font-weight:600}
  .front__photo{left:0;top:80px;width:460px;height:272px;background:linear-gradient(90deg,#cfd3d6 0%,#b9bec2 48%,#3b3430 50%,#dfe7ee 54%,#b8cfe0 80%,#2c6f9d 100%)}
  .intro{left:0;top:345px;width:238px;height:305px;background:var(--panel)}
  .intro__title{left:12px;top:8px;font-size:14px;line-height:16px;color:var(--white);font-family:"Roboto Condensed",sans-serif}
  .intro__title strong{color:var(--blue);font-weight:700;letter-spacing:.3px}
  .intro__copy{left:12px;top:46px;width:218px;font-size:9.3px;line-height:12px;color:#e6e6e6;text-align:justify}
  .intro__copy em{font-style:normal;color:var(--blue)}
  .intro__copy b{color:var(--blue)}
  .device{top:110px;width:69px;text-align:center}
  .device .ph{position:relative;width:69px;height:58px;border-radius:6px}
  .device span{display:block;margin-top:6px;font-size:8.5px;color:#ddd}
  .focus{left:0;top:193px;width:238px;text-align:center;font-family:"Roboto Condensed",sans-serif;font-size:8px;line-height:14px;color:var(--blue);text-transform:uppercase;font-weight:700}
  .contact{left:0;top:250px;width:238px;height:55px;background:linear-gradient(180deg,var(--blue),var(--blue-deep));text-align:center;color:var(--white)}
  .contact p{font-family:"Roboto Condensed",sans-serif;font-size:10px;line-height:11px;margin-top:6px;text-transform:uppercase}
  .contact .phone{font-size:22px;font-weight:700;margin-top:2px;display:flex;justify-content:center;align-items:center;gap:6px;line-height:1}
  .aim__title{left:246px;top:362px;font-size:20px;font-family:"Open Sans",sans-serif;color:var(--ink);font-weight:600}
  .aim__title span{color:var(--blue);font-weight:400}
  .aim__copy{left:246px;top:393px;width:206px;font-size:8.6px;line-height:11.6px;text-align:justify;color:#333}
  .family{left:238px;top:533px;width:222px;height:102px;background:linear-gradient(135deg,#e5d6c8,#c28f7a 50%,#8c9db0)}
  .web{left:238px;top:635px;width:222px;height:15px;background:var(--white);font-size:8.5px;color:var(--navy);display:flex;align-items:center;justify-content:center;gap:5px}
  .web i{width:8px;height:8px;border-radius:50%;background:var(--navy);display:inline-block}

  /* back */
  .band{left:0;top:90px;width:460px;height:40px;background:var(--blue);color:var(--white);font-family:"Roboto Condensed",sans-serif;font-size:30px;line-height:40px;text-align:center;letter-spacing:.5px}
  .band b{font-weight:700}
  .grid{left:0;top:138px;width:460px;height:450px;display:grid;grid-template-columns:repeat(3,1fr);grid-template-rows:repeat(3,1fr)}
  .tile{position:relative;border-right:1px solid var(--rule);border-bottom:1px solid var(--rule);text-align:center;padding-top:13px}
  .tile:nth-child(3n){border-right:0}
  .tile:nth-child(n+7){border-bottom:0}
  .tile .ph{position:relative;margin:0 auto;width:112px;height:94px;border-radius:12px 0 12px 0}
  .tile h3{font-family:"Roboto Condensed",sans-serif;font-weight:700;font-size:12px;line-height:14px;color:var(--navy);margin-top:9px}
  .back__foot{left:0;top:585px;width:460px;height:65px}
  .email{left:30px;top:634px;font-size:10px;color:var(--white);display:flex;align-items:center;gap:5px}
  .bigphone{left:272px;top:602px;font-family:"Roboto Condensed",sans-serif;font-weight:700;font-size:28px;color:var(--white);display:flex;align-items:center;gap:8px}
</style>
</head>
<body>

<section class="flyer flyer--front">
  <p class="abs kicker"><b>SMART DEVICE</b> INTEGRATION</p>
  <div class="brand" style="left:276px;top:22px">
    <span class="brand__dot"></span><span class="brand__name">Bright Hollow</span>
  </div>
  <svg class="abs" style="left:0;top:64px" width="460" height="20" viewBox="0 0 460 20">
    <polygon points="0,4 240,4 252,12 460,12 460,16 250,16 238,8 0,8" fill="var(--blue)"/>
  </svg>
  <div class="ph front__photo" role="img" aria-label="Wall-mounted smart home touch panel beside a bright living room with blue sofas"></div>

  <svg class="abs" style="left:0;top:330px" width="460" height="20" viewBox="0 0 460 20">
    <polygon points="0,15 225,15 240,15 250,6 460,6 460,20 0,20" fill="var(--white)"/>
    <polygon points="0,15 228,15 240,4 460,4 460,7 242,7 230,18 0,18" fill="var(--blue)"/>
  </svg>

  <div class="abs intro" style="top:348px">
    <h2 class="abs intro__title">YOUR SMART HOME<br><strong>INTEGRATION PROFESSIONALS</strong></h2>
    <p class="abs intro__copy">We'll show you how these speaker powered voice activated <em>Smart Assitants</em> hold the key to your New Smart Home. Start building your new Smart Home with thesedevices starting from <b>$50.00</b></p>
    <div class="abs device" style="left:10px"><span class="ph" role="img" aria-label="Cylindrical smart speaker" style="background:linear-gradient(180deg,#f1f1f1,#3a3a3a)"></span><span>Carrowby Orb</span></div>
    <div class="abs device" style="left:85px"><span class="ph" role="img" aria-label="Compact white smart speaker" style="background:linear-gradient(180deg,#fafafa,#b9b6b2)"></span><span>Pellix Hub</span></div>
    <div class="abs device" style="left:160px"><span class="ph" role="img" aria-label="Round fabric smart speaker" style="background:linear-gradient(180deg,#dcdcdc,#4a4c50)"></span><span>Orchard Pod</span></div>
    <p class="abs focus">We are focused on delivering affordable and easily usable<br>devices for your home and office<br>Wireless smart home - no need for pre-wired cabling</p>
    <div class="abs contact" style="top:247px">
      <p>Contact us to find out how<br>— We can help you —</p>
      <div class="phone">
        <svg width="16" height="16" viewBox="0 0 24 24"><path d="M6.6 10.8a15 15 0 0 0 6.6 6.6l2.2-2.2a1 1 0 0 1 1-.25 11.4 11.4 0 0 0 3.6.57 1 1 0 0 1 1 1V20a1 1 0 0 1-1 1A17 17 0 0 1 3 4a1 1 0 0 1 1-1h3.5a1 1 0 0 1 1 1c0 1.25.2 2.45.57 3.57a1 1 0 0 1-.25 1z" fill="#fff"/></svg>
        0400 555 019
      </div>
    </div>
  </div>

  <h2 class="abs aim__title">Our <span>Aim</span></h2>
  <p class="abs aim__copy">Our aim is to bring affordable smart home products to everyone, offering seamless integration and reliability. With a wide range of available cost options, outstanding service and experience, we are the solution for all your smart home technology solutions. We are a passionate group of tech specialists who have years of experience with installing, using and troubleshooting residential and industrial technology systems</p>
  <div class="ph family" role="img" aria-label="Family gathered on a sofa using tablets and a laptop"></div>
  <p class="abs web"><i></i>www.brighthollow-example.net</p>
</section>

<section class="flyer flyer--back">
  <div class="brand" style="left:128px;top:26px">
    <span class="brand__dot"></span><span class="brand__name">Bright Hollow</span>
  </div>
  <h1 class="abs band"><b>SMART HOME</b> SPECIALISTS</h1>
  <div class="abs grid">
    <div class="tile"><span class="ph" role="img" aria-label="Hand-drawn light bulb illustration" style="background:linear-gradient(135deg,#f4f4f4,#e9c24a 60%,#c9ccd0)"></span><h3>Home Automation</h3></div>
    <div class="tile"><span class="ph" role="img" aria-label="Smart speaker with floating home icons" style="background:linear-gradient(180deg,#9a6a3c,#3a2a22 60%,#1d6fa8)"></span><h3>Voice Control With Nimbo</h3></div>
    <div class="tile"><span class="ph" role="img" aria-label="Phone app unlocking a smart door lock" style="background:linear-gradient(135deg,#2a2a2a,#6b6b6b 60%,#3b3b3b)"></span><h3>Keyless Entry</h3></div>
    <div class="tile"><span class="ph" role="img" aria-label="Home theatre screen with purple accent lighting" style="background:linear-gradient(135deg,#b56b74,#2b1f2e 60%,#4b3c8c)"></span><h3>Home Theatre Design</h3></div>
    <div class="tile"><span class="ph" role="img" aria-label="Bedroom with motorised blinds and a control panel" style="background:linear-gradient(135deg,#eef0f1,#b9bec2 60%,#7d7f82)"></span><h3>Blind and Curtain<br>Automation</h3></div>
    <div class="tile"><span class="ph" role="img" aria-label="Smartphone showing a video doorbell feed" style="background:linear-gradient(135deg,#6f7277,#e4e4e4 55%,#c9b48a)"></span><h3>Video Doorbell and<br>Intercom</h3></div>
    <div class="tile"><span class="ph" role="img" aria-label="Modern house with an open garage" style="background:linear-gradient(180deg,#d5e3ef,#8a8d90 55%,#c98b4b)"></span><h3>Smart Garage Doors</h3></div>
    <div class="tile"><span class="ph" role="img" aria-label="Media library shown on a large television" style="background:linear-gradient(180deg,#1e7fb8,#14365e 60%,#1b2b40)"></span><h3>Media Entertainmen</h3></div>
    <div class="tile"><span class="ph" role="img" aria-label="Floor plan with ceiling speakers in each room" style="background:linear-gradient(135deg,#c9d6cf,#8fa59b 55%,#b7bcc0)"></span><h3>Multiroom Audio</h3></div>
  </div>
  <svg class="abs back__foot" width="460" height="65" viewBox="0 0 460 65">
    <polygon points="270,2 460,2 460,5 272,5 245,34 0,34 0,31 243,31" fill="var(--blue)"/>
    <polygon points="274,9 460,9 460,65 0,65 0,39 249,39" fill="var(--navy)"/>
  </svg>
  <p class="abs email">
    <svg width="12" height="12" viewBox="0 0 24 24"><circle cx="12" cy="12" r="11" fill="#fff"/><rect x="6" y="8" width="12" height="8" fill="var(--navy)"/><path d="M6 8l6 5 6-5" stroke="#fff" stroke-width="1.3" fill="none"/></svg>
    info@brighthollow-example.net
  </p>
  <p class="abs bigphone">
    <svg width="24" height="24" viewBox="0 0 24 24"><path d="M6.6 10.8a15 15 0 0 0 6.6 6.6l2.2-2.2a1 1 0 0 1 1-.25 11.4 11.4 0 0 0 3.6.57 1 1 0 0 1 1 1V20a1 1 0 0 1-1 1A17 17 0 0 1 3 4a1 1 0 0 1 1-1h3.5a1 1 0 0 1 1 1c0 1.25.2 2.45.57 3.57a1 1 0 0 1-.25 1z" fill="#fff"/></svg>
    0400 555 019
  </p>
</section>

</body>
</html>
```